Plakat für Tanzschule
Zielgruppe
Wir sind eine Tanzschule
Hallo,
ich benötige ein professionelles Design für ein Schild im Format 2 Meter breit × 1 Meter hoch (Querformat), das von einem stark frequentierten Parkplatz aus gut sichtbar ist.
✅ Ziel:
Gestaltung eines aufmerksamkeitsstarken, eleganten und energiegeladenen Werbeschilds
Das Schild soll sofort zeigen, worum es geht (Tanzstile) und zum kostenlosen Schnuppern motivieren
Die Gestaltung soll hochwertig und grafisch modern wirken
Bild / Hintergrund:
Ich habe einen ersten Design-Vorschlag hochgeladen (Screenshot)
⚠️ Ursprünglich hatte ich vor, ein bereits ausgeschnittenes und bearbeitetes Bild zu liefern (z. B. Unreinheiten und Störungen im Bild zu glätten oder zu entfernt und Zähne etwas weißer). Das kann ich jetzt leider doch nicht nachreichen. Daher müsste doch die Bearbeitung des Bildes mit übernommen werden.
✏️ Textinhalte (hierarchisch sortiert):
TANZSCHULE
Salsa · Bachata · Kizomba · Zouk
Jetzt Gratis Schnuppern!
Ritmo y Alma (Markenname)
www.ritmo-y-alma.de
???? Wichtig:
Die wichtigsten Inhalte (Tanzarten & CTA) müssen sofort erfassbar sein
Design bitte auf Fernwirkung, klare Lesbarkeit und modernes visuelles Layout ausrichten
Text in sinnvollen Größenabstufungen und mit sauberer visueller Hierarchie
Unsere eigentliche Hauptfarbe ist #ad194f, bis jetzt habe ich aber noch keine schöne Möglichkeit gefunden, in das aktuelle Design einzuarbeiten.
????️ Endformat & Übergabe:
Bitte das fertige Layout als .afdesign Datei (Affinity Designer) liefern
Optional PSD, EPS

```html
<!DOCTYPE html>
<html lang="de">
<head>
<meta charset="utf-8">
<title>Ritmo y Alma – Tanzschule Schild</title>
<link rel="stylesheet" href="https://fonts.googleapis.com/css2?family=Barlow+Condensed:wght@500;700&family=Barlow:wght@400&display=swap">
<style>
  :root {
    --brand: #ad194f;
    --brand-deep: #9c1747;
    --brand-light: #e0447f;
    --ink: #1d1d1b;
    --paper: #ffffff;
    --backdrop: #d0d1d7;
    --photo-a: #c2245f;
    --photo-b: #6f6a5e;
  }
  html, body {
    margin: 0;
    width: 1200px;
    height: 1111px;
    overflow: hidden;
    background: var(--backdrop);
  }
  .sign {
    position: absolute;
    left: 40px;
    top: 275px;
    width: 1120px;
    height: 560px;
    display: block;
  }
  .sign__panel { fill: var(--paper); }
  .headline {
    font-family: "Barlow Condensed", sans-serif;
    font-weight: 700;
    fill: var(--brand);
  }
  .styles {
    font-family: "Barlow Condensed", sans-serif;
    font-weight: 700;
    fill: var(--ink);
  }
  .cta__label {
    font-family: "Barlow Condensed", sans-serif;
    font-weight: 700;
    fill: var(--paper);
  }
  .brand__name {
    font-family: "Barlow Condensed", sans-serif;
    font-weight: 500;
    fill: var(--brand);
  }
  .brand__tagline {
    font-family: "Barlow", sans-serif;
    font-weight: 400;
    fill: var(--ink);
  }
  .brand__dot { fill: var(--brand); }
  .website {
    font-family: "Barlow Condensed", sans-serif;
    font-weight: 500;
    fill: var(--ink);
  }
  .arch { fill: var(--brand); }
</style>
</head>
<body>
<svg class="sign" viewBox="0 0 1120 560" xmlns="http://www.w3.org/2000/svg">
  <defs>
    <linearGradient id="cta-fill" x1="0" y1="0" x2="1" y2="0">
      <stop offset="0" stop-color="var(--brand-deep)"/>
      <stop offset="0.5" stop-color="var(--brand-light)"/>
      <stop offset="1" stop-color="var(--brand-deep)"/>
    </linearGradient>
    <linearGradient id="photo-fill" x1="0" y1="0" x2="0" y2="1">
      <stop offset="0" stop-color="var(--photo-a)"/>
      <stop offset="0.55" stop-color="var(--brand)"/>
      <stop offset="1" stop-color="var(--photo-b)"/>
    </linearGradient>
  </defs>

  <rect class="sign__panel" x="0" y="0" width="1120" height="560"/>

  <path class="arch" d="M663 560 V243 A206 206 0 0 1 1075 243 V560 Z"/>
  <path d="M663 560 V243 A206 206 0 0 1 1075 243 V560 Z" fill="url(#photo-fill)" opacity="0.85"
        role="img" aria-label="Foto: lachendes Tanzpaar in Bewegung, sie mit fliegenden blonden Haaren, er im grünen T-Shirt"/>

  <text class="headline" x="47" y="156" font-size="148" textLength="594" lengthAdjust="spacingAndGlyphs">TANZSCHULE</text>
  <text class="styles" x="84" y="249" font-size="96" textLength="511" lengthAdjust="spacingAndGlyphs">SALSA · BACHATA</text>
  <text class="styles" x="113" y="342" font-size="96" textLength="469" lengthAdjust="spacingAndGlyphs">KIZOMBA · ZOUK</text>

  <g class="cta">
    <rect x="46" y="365" width="589" height="67" rx="33.5" fill="url(#cta-fill)"/>
    <text class="cta__label" x="114" y="415" font-size="50" textLength="453" lengthAdjust="spacingAndGlyphs">JETZT GRATIS SCHNUPPERN!</text>
  </g>

  <g class="brand">
    <circle class="brand__dot" cx="58" cy="482" r="9"/>
    <text class="brand__name" x="76" y="494" font-size="38">Ritmo y Alma</text>
    <text class="brand__tagline" x="76" y="515" font-size="10">Tanzschule im Herzen Freiburgs</text>
  </g>

  <text class="website" x="334" y="497" font-size="36" textLength="291" lengthAdjust="spacingAndGlyphs">WWW.RITMO-Y-ALMA.DE</text>
</svg>
</body>
</html>
```